Information Security Company Business Cards

Using our included logo, we need a business card design. It should have standard contact information such as :

Ravi Tanner
Senior Security Engineer
ravi.tanner@quorvex-hub.com
877.640.3958

Maybe include the website "www.quorvex-hub.com" that we will be redesigning soon.??

open to suggestions of course...

Target Market(s)

Our customers are small to large companies. Generally health-care, financial, insurance and the like.

Industry/Entity Type

Business

Font styles to use
Other font styles liked:
• Something that works with the logo

Requirements
Must have
• Colors should flow with the logo if possible. Or at least we think it should.

```html
<!DOCTYPE html>
<html lang="en">
<head>
<meta charset="utf-8">
<title>Quorvex Hub Business Cards</title>
<link rel="stylesheet" href="https://fonts.googleapis.com/css2?family=Exo+2:wght@300;400;800&display=swap">
<style>
  :root {
    --bg: #8a8d94;
    --royal: #1a1f96;
    --ink: #1f1f22;
    --paper: #ffffff;
    --muted: #cfd0d6;
  }
  html, body {
    margin: 0;
    width: 1200px;
    height: 960px;
    overflow: hidden;
    background: var(--bg);
    font-family: "Exo 2", sans-serif;
  }
  .stage {
    position: relative;
    width: 1200px;
    height: 960px;
  }
  .card {
    position: absolute;
    top: 200px;
    width: 330px;
    height: 560px;
    overflow: hidden;
    background: var(--paper);
    box-shadow: 0 14px 30px rgba(0,0,0,.3);
  }
  .card-front { left: 220px; }
  .card-back { left: 650px; }
  .card svg.shapes {
    position: absolute;
    inset: 0;
  }
  .brand {
    position: absolute;
    left: 0;
    right: 0;
    display: flex;
    flex-direction: column;
    align-items: center;
    gap: 14px;
  }
  .brand-dot {
    width: 74px;
    height: 74px;
    border-radius: 50%;
    border: 6px solid currentColor;
    box-sizing: border-box;
  }
  .brand-name {
    font-weight: 800;
    font-size: 34px;
    letter-spacing: 1px;
    line-height: 1;
    text-transform: uppercase;
    text-align: center;
  }
  .card-front .brand { top: 150px; color: var(--paper); }
  .card-back .brand { top: 48px; color: var(--ink); }
  .contact {
    position: absolute;
    left: 0;
    right: 0;
    top: 340px;
    text-align: center;
    color: var(--paper);
  }
  .contact-name {
    font-size: 22px;
    font-weight: 400;
    letter-spacing: 1px;
    text-transform: uppercase;
    margin: 0;
  }
  .contact-title {
    font-size: 12px;
    font-weight: 300;
    font-style: italic;
    color: var(--muted);
    margin: 4px 0 22px;
  }
  .contact-line {
    font-size: 15px;
    font-weight: 300;
    margin: 6px 0;
  }
</style>
</head>
<body>
<main class="stage">
  <section class="card card-front">
    <svg class="shapes" width="330" height="560" viewBox="0 0 330 560">
      <path d="M0 0H330V400Q170 480 0 410Z" fill="var(--royal)"/>
    </svg>
    <div class="brand">
      <span class="brand-dot"></span>
      <span class="brand-name">Quorvex Hub</span>
    </div>
  </section>

  <section class="card card-back">
    <svg class="shapes" width="330" height="560" viewBox="0 0 330 560">
      <path d="M0 215Q240 225 330 470V560H0Z" fill="var(--royal)"/>
      <path d="M0 240Q215 250 300 560H0Z" fill="var(--ink)"/>
    </svg>
    <div class="brand">
      <span class="brand-dot"></span>
      <span class="brand-name">Quorvex Hub</span>
    </div>
    <div class="contact">
      <p class="contact-name">Ravi Tanner</p>
      <p class="contact-title">Senior Security Engineer</p>
      <p class="contact-line">877.640.3958</p>
      <p class="contact-line">ravi.tanner@quorvex-hub.com</p>
      <p class="contact-line">www.quorvex-hub.com</p>
    </div>
  </section>
</main>
</body>
</html>
```